I need a book cover for a 6x9 book. The front cover information (title and author) is below, and the back cover information will be given to the winning designer. I am wanting something vibrant and bright, and I am open to your creativity, but I do not want any pictures of people on the cover. Save room for the barcode on the back cover.
Title:
Oops! Wrong Turn?
Quiet Rooms Explained: Notes on Patient Gardening Habits
Author:
Marisol Tembe

```html
<!DOCTYPE html>
<html lang="en">
<head>
<meta charset="utf-8">
<title>Oops! Wrong Turn? — Book Cover</title>
<link rel="stylesheet" href="https://fonts.googleapis.com/css2?family=Bebas+Neue&display=swap">
<style>
  :root {
    --ink: #000000;
    --lime: #7cff7f;
    --lemon: #edf535;
    --paper: #ffffff;
    --rule-glow: #f4ff3a;
  }
  html, body {
    margin: 0;
    padding: 0;
    width: 800px;
    height: 1200px;
    overflow: hidden;
    background: var(--ink);
  }
  .cover {
    position: relative;
    width: 800px;
    height: 1200px;
    background: var(--ink);
    font-family: "Bebas Neue", "Oswald", sans-serif;
    overflow: hidden;
  }
  .title {
    margin: 0;
    font-weight: 400;
  }
  .title-line {
    position: absolute;
    left: 0;
    width: 800px;
    text-align: center;
    line-height: 1;
    white-space: nowrap;
  }
  .title-line--top {
    top: 55px;
    font-size: 168px;
    color: var(--lime);
    letter-spacing: 1px;
  }
  .title-line--bottom {
    top: 178px;
    font-size: 302px;
    color: var(--lemon);
    letter-spacing: 14px;
  }
  .rule {
    position: absolute;
    left: 181px;
    width: 444px;
    height: 3px;
    background: linear-gradient(90deg, transparent, var(--rule-glow) 50%, transparent);
  }
  .rule--upper { top: 468px; }
  .rule--lower { top: 587px; }
  .subtitle {
    position: absolute;
    top: 484px;
    left: 0;
    width: 800px;
    margin: 0;
    text-align: center;
    font-weight: 400;
    font-size: 44px;
    line-height: 46px;
    letter-spacing: 2px;
    color: var(--paper);
  }
  .subtitle-accent {
    display: block;
    color: var(--lime);
  }
  .artwork {
    position: absolute;
    left: 102px;
    top: 638px;
    width: 594px;
    height: 452px;
    border-radius: 46% 46% 40% 40%;
    background: linear-gradient(100deg, #f0c56e 0%, #e5ff6b 22%, #81c576 40%, #6680d0 62%, #7c5fe0 78%, #d48bd6 100%);
    opacity: 0.9;
  }
  .author {
    position: absolute;
    top: 1112px;
    left: 0;
    width: 800px;
    margin: 0;
    text-align: center;
    font-weight: 400;
    font-size: 54px;
    line-height: 1;
    letter-spacing: 11px;
    color: var(--paper);
  }
</style>
</head>
<body>
  <main class="cover">
    <h1 class="title">
      <span class="title-line title-line--top">Oops! Wrong</span>
      <span class="title-line title-line--bottom">Turn?</span>
    </h1>
    <div class="rule rule--upper"></div>
    <h2 class="subtitle">
      QUIET ROOMS EXPLAINED: NOTES ON
      <span class="subtitle-accent">PATIENT GARDENING HABITS</span>
    </h2>
    <div class="rule rule--lower"></div>
    <div class="artwork" role="img" aria-label="Cluster of overlapping translucent speech bubbles in yellow, orange, green, blue, purple and pink"></div>
    <p class="author">MARISOL TEMBE</p>
  </main>
</body>
</html>
```